Cleaning Service Company In need of Good Web presence.

The company is a cleaning service company which provides professional staff and service for cleaning. This is a project to build a site that is both solid and a strong recognition of our organization. It is supposed to show quality, cleanliness, professionalism. The use of images and art for imagery is all good just to have a site that is consistent and solid. There might be a chance to make stationary, logo and business cars if someone feels they can build a brand that is consistent. The image we are going for is clean solid and to stand out. Finally stationary should not be expensive to print.

Current logo is attached and can be used or can be made more creative.

Target Market(s)

Corporate and Government entities, that will feel that this company has a brand that sets it apart from the rest. The company is new so the modification of the logo will not be an issue if a more solid brand come out of this project. The idea is to have a clean consistent product that stands our from others in terms of website, stationary, etc

Industry/Entity Type

Cleaning Service

Contact Information for Business Card

P.O.Box 51947
Riffa
Kingdom of Bahrain

Logo Text

Brightmoor Facility Care

Number of Pages Required

4 page

Font styles to use
Sans Serif

Colors
abd036
cadf82
eaf2ce
9bcb3b

Requirements
Must have
• Green Color to be used in order to stick to the name. Also the creativity and boldness in an elegant manner.
Nice to have
• Arabic name of company
• برايتمور فاسيليتي كير ذ.م.م
• if cannot be put at least make a location should be chosen
• Also could be a bit of 3D given to the logo if it could stay elegent.
Should not have
• Should not show people cleaning.

```html
<!DOCTYPE html>
<html lang="en">
<head>
<meta charset="utf-8">
<title>Brightmoor Facility Care</title>
<link href="https://fonts.googleapis.com/css2?family=Open+Sans:wght@400;600;700&display=swap" rel="stylesheet">
<style>
:root{
  --green:#9bcb3b;
  --green-2:#abd036;
  --green-soft:#cadf82;
  --green-pale:#eaf2ce;
  --orange:#e9a24a;
  --blue-btn:#6fa1c9;
  --ink:#555;
  --footer:#2b3a44;
  --footer-dark:#1f2a31;
  --footer-text:#b8c2c8;
}
*{box-sizing:border-box;margin:0;padding:0}
html,body{width:1200px;height:1200px;overflow:hidden;background:#fff;font-family:"Open Sans",sans-serif;color:var(--ink)}
.page{position:absolute;left:391px;top:0;width:480px;height:1200px;background:#fff}
.abs{position:absolute}

/* hero */
.hero{left:0;top:0;width:480px;height:178px;background:linear-gradient(180deg,#4f7a63 0%,#6f9478 45%,#5f8572 75%,#3f5d52 100%)}
.brand{left:66px;top:10px;display:flex;align-items:center;gap:5px;font-size:7px;font-weight:700;color:#fff}
.brand .dot{width:14px;height:14px;border-radius:50%;background:var(--green)}
.nav{right:53px;top:11px;display:flex;gap:12px;font-size:5px;color:#fff}
.hero-title{left:0;width:480px;top:73px;text-align:center;font-size:15px;font-weight:700;color:#fff}
.arrow{top:80px;width:14px;height:14px;border-radius:50%;background:rgba(255,255,255,.15);color:var(--orange);font-size:7px;text-align:center;line-height:14px}
.btn-more{left:214px;top:130px;width:50px;height:16px;background:var(--blue-btn);color:#fff;font-size:5px;font-weight:700;text-align:center;line-height:16px}
.hero-dots{left:0;width:480px;top:156px;display:flex;justify-content:center;align-items:center;gap:7px}
.hero-dots i{width:2px;height:2px;border-radius:50%;background:#fff;display:block}
.hero-dots i.on{width:8px;height:8px;border:1px solid #fff;background:none;position:relative}

/* services */
.sec-title{left:0;width:480px;text-align:center;font-size:8px;font-weight:700;color:var(--green)}
.sec-sub{left:0;width:480px;text-align:center;font-size:5px;color:#666}
.service{width:190px}
.service svg{position:absolute;left:-13px;top:-1px}
.service h4{font-size:4.5px;font-weight:600;color:var(--green);margin-bottom:4px}
.service p{font-size:3.9px;line-height:7px;color:#777;width:152px}

/* about */
.about-photo{left:0;top:414px;width:239px;height:200px;background:linear-gradient(180deg,#8fa79c 0%,#a9bcb1 50%,#2d3a33 78%,#1c241f 100%)}
.about{left:240px;top:414px;width:240px;height:200px;background:var(--green-soft)}
.about h3{position:absolute;left:25px;top:29px;font-size:8px;font-weight:600;color:#fff}
.about p{position:absolute;left:25px;width:165px;font-size:3.9px;line-height:7.8px;color:#fff}
.btn-read{left:25px;top:159px;width:47px;height:14px;background:var(--orange);color:#fff;font-size:4.5px;text-align:center;line-height:14px}

/* work */
.orn{left:204px;top:659px;width:72px;height:8px}
.work-sub{left:90px;width:300px;top:673px;text-align:center;font-size:4.8px;line-height:7.5px;color:var(--green-soft)}
.tabs{top:703px;left:149px;display:flex;gap:14px;font-size:4.8px;color:#333;align-items:center}
.tabs .on{background:var(--green);color:#fff;padding:2px 6px}
.grid{left:0;top:722px;width:480px;height:181px;display:grid;grid-template-columns:repeat(4,120px);grid-template-rows:90px 91px}
.grid div{width:100%;height:100%}
.g1{background:linear-gradient(180deg,#5a5f3a,#c7b968 60%,#3d3a22)}
.g2{background:linear-gradient(180deg,#5c8fc4,#c9d7e6 55%,#8aa6b8)}
.g3{background:var(--green);position:relative;color:#fff;text-align:center}
.g3 .ov{position:absolute;left:0;right:0;top:29px;height:auto}
.g3 .eye{width:11px;height:11px;border:1px solid rgba(255,255,255,.7);border-radius:50%;margin:0 auto 6px}
.g3 b{display:block;font-size:5.2px;line-height:7px}
.g3 span{display:block;font-size:4px;line-height:6px;margin-top:1px}
.g4{background:linear-gradient(180deg,#6f8a9a,#2f4450 60%,#4a2a2a)}
.g5{background:linear-gradient(180deg,#2f6da8,#4f8a3c 70%,#2d6b2c)}
.g6{background:linear-gradient(180deg,#9fb0bf,#d8d3b8 50%,#6a6a55)}
.g7{background:linear-gradient(180deg,#c9c7a4,#a58a5b 60%,#6e5a38)}
.g8{background:linear-gradient(180deg,#2e8a63,#3e9a6e)}

/* testimonials */
.quote{width:145px;height:48px;background:var(--green-soft);padding:6px 8px;font-size:3.9px;line-height:7.3px;font-style:italic;color:#777}
.person{display:flex;align-items:center;gap:7px;font-size:3.9px;color:#444}
.person i{width:7px;height:7px;background:#3a2f4a;border-radius:50% 50% 1px 1px;display:block}
.t-dots{left:0;width:480px;top:1042px;display:flex;justify-content:center;gap:2px}
.t-dots i{width:3px;height:3px;border-radius:50%;background:#ccc;display:block}
.t-dots i.on{background:none;border:1px solid var(--blue-btn);width:4px;height:4px}

/* footer */
.footer{left:0;top:1062px;width:480px;height:112px;background:var(--footer)}
.footer h5{font-size:6.2px;font-weight:400;color:#fff;margin-bottom:6px}
.footer p{font-size:3.9px;line-height:6.5px;color:var(--footer-text)}
.fcol{position:absolute;top:23px}
.contact-row{display:flex;align-items:center;gap:8px;font-size:4px;color:#fff;margin-top:3px}
.tweet{display:flex;gap:5px;margin-bottom:3px}
.tweet i{width:4px;height:4px;border-radius:50%;background:#4aa3df;display:block;margin-top:3px;flex:none}
.tweet em{font-style:normal;color:#4aa3df}
.news{display:flex;margin-top:8px}
.news span{width:58px;height:11px;background:#1e282e;font-size:3.8px;color:#aaa;line-height:11px;padding-left:5px}
.news b{width:27px;height:11px;background:#5ba8d8;font-size:3.8px;color:#fff;font-weight:400;line-height:11px;text-align:center}
.bottom{left:0;top:1174px;width:480px;height:26px;background:var(--footer-dark)}
.bottom p{position:absolute;left:0;width:480px;top:10px;text-align:center;font-size:4px;color:#aab}
.social{position:absolute;right:53px;top:8px;display:flex;gap:3px}
.social i{width:8px;height:8px;background:#4a8fc4;display:block}
.social i:nth-child(2),.social i:nth-child(3){background:#3c4c58}
</style>
</head>
<body>
<div class="page">

  <section class="abs hero" role="img" aria-label="Green-tinted photo of a cloudy sky over mountains"></section>
  <div class="abs brand"><span class="dot"></span>Brightmoor Facility Care</div>
  <nav class="abs nav"><span>Home</span><span>Services</span><span>About</span><span>Portfolio</span><span>Testimonials</span><span>Contact</span></nav>
  <h1 class="abs hero-title">Brightmoor Facility Care W.L.L</h1>
  <div class="abs arrow" style="left:59px">‹</div>
  <div class="abs arrow" style="left:406px">›</div>
  <div class="abs btn-more">SHOW MORE</div>
  <div class="abs hero-dots"><i></i><i class="on"></i><i></i></div>

  <h2 class="abs sec-title" style="top:201px">SERVICES</h2>
  <p class="abs sec-sub" style="top:213px">Lorem ipsum dolor sit amet, consectetuer adipiscing elit. Aenean commodo ligula eget dolor.</p>

  <div class="abs service" style="left:80px;top:246px">
    <svg width="10" height="10" viewBox="0 0 10 10" fill="none" stroke="#e9a24a" stroke-width=".8"><path d="M1 1l8 8M9 1L1 9M1 3l2-2M7 9l2-2"/></svg>
    <h4>SERVICE ONE</h4><p>Lorem ipsum dolor sit amet, consectetuer adipiscing elit. Aenean commodo ligula eget dolor. Aenean massa. Cum sociis natoque penatibus et magnis dis parturient montes, nascetur ridiculus mus.</p></div>
  <div class="abs service" style="left:80px;top:300px">
    <svg width="10" height="10" viewBox="0 0 10 10" fill="none" stroke="#8aa03a" stroke-width=".8"><path d="M5 1l4 2-4 2-4-2zM1 5l4 2 4-2M1 7l4 2 4-2"/></svg>
    <h4>SERVICE TWO</h4><p>Lorem ipsum dolor sit amet, consectetuer adipiscing elit. Aenean commodo ligula eget dolor. Aenean massa. Cum sociis natoque penatibus et magnis dis parturient montes, nascetur ridiculus mus.</p></div>
  <div class="abs service" style="left:80px;top:354px">
    <svg width="10" height="10" viewBox="0 0 10 10" fill="none" stroke="#8aa03a" stroke-width=".8"><circle cx="5" cy="5" r="4"/><path d="M5 3v4"/></svg>
    <h4>SERVICE FOUR</h4><p>Lorem ipsum dolor sit amet, consectetuer adipiscing elit. Aenean commodo ligula eget dolor. Aenean massa. Cum sociis natoque penatibus et magnis dis parturient montes, nascetur ridiculus mus.</p></div>
  <div class="abs service" style="left:277px;top:246px">
    <svg width="10" height="10" viewBox="0 0 10 10" fill="none" stroke="#8aa03a" stroke-width=".8"><path d="M1 2h2l1 5h5l1-4H3.5"/><circle cx="4.5" cy="8.5" r=".6"/><circle cx="8" cy="8.5" r=".6"/></svg>
    <h4>SERVICE THREE</h4><p>Lorem ipsum dolor sit amet, consectetuer adipiscing elit. Aenean commodo ligula eget dolor. Aenean massa. Cum sociis natoque penatibus et magnis dis parturient montes, nascetur ridiculus mus.</p></div>
  <div class="abs service" style="left:277px;top:300px">
    <svg width="10" height="10" viewBox="0 0 10 10" fill="none" stroke="#8aa03a" stroke-width=".8"><rect x="1" y="1.5" width="8" height="5.5"/><path d="M2.5 5l2-2 1.5 1.5 2-2M5 7v2"/></svg>
    <h4>SERVICE FIVE</h4><p>Lorem ipsum dolor sit amet, consectetuer adipiscing elit. Aenean commodo ligula eget dolor. Aenean massa. Cum sociis natoque penatibus et magnis dis parturient montes, nascetur ridiculus mus.</p></div>
  <div class="abs service" style="left:277px;top:354px">
    <svg width="10" height="10" viewBox="0 0 10 10" fill="none" stroke="#8aa03a" stroke-width=".8"><circle cx="5" cy="4" r="3"/><path d="M4 7.5h2M4.3 9h1.4"/></svg>
    <h4>SERVICE SIX</h4><p>Fusce velit magna, rutrum id pellentesque in, imperdiet rutrum neque. Vestibulum elementum ex ullamcorper ligula vulputate, non malesuada nisi ullamcorper. Curabitur tellus ligula, laoreet vitae lectus vitae.</p></div>

  <div class="abs about-photo" role="img" aria-label="Silhouette of a person standing on a hill at dusk"></div>
  <section class="abs about">
    <h3>ABOUT US</h3>
    <p style="top:50px">Lorem ipsum dolor sit amet, consectetur adipiscing elit. Praesent dui massa, condimentum a nisl quis, tristique efficitur erat. Aenean ut suscipit urna. Donec efficitur tristique lobortis. Nullam eu efficitur lacus, et blandit tellus. Mauris viverra condimentum tellus vitae sollicitudin. Mauris quis mattis urna. Suspendisse auctor magna quis ipsum ultrices scelerisque. Vestibulum quis hendrerit enim. Aenean viverra aliquam ex, sed ornare risus porta in.</p>
    <p style="top:104px">Aenean ut suscipit urna. Donec efficitur tristique lobortis. Nullam eu efficitur lacus, et blandit tellus. Mauris viverra condimentum tellus vitae sollicitudin. Mauris quis mattis urna. Suspendisse auctor magna quis ipsum ultrices scelerisque. Vestibulum quis hendrerit enim. Aenean viverra aliquam ex, sed ornare risus porta in.</p>
    <div class="abs btn-read">READ MORE</div>
  </section>

  <h2 class="abs sec-title" style="top:644px">OUR WORK</h2>
  <svg class="abs orn" viewBox="0 0 72 8"><line x1="0" y1="4" x2="30" y2="4" stroke="#f0c48a" stroke-width=".6"/><line x1="42" y1="4" x2="72" y2="4" stroke="#f0c48a" stroke-width=".6"/><circle cx="36" cy="4" r="2.5" fill="#e9a24a"/></svg>
  <p class="abs work-sub">Lorem ipsum dolor sit amet, consectetuer adipiscing elit. Aenean commodo ligula eget dolor. Aenean massa. Cum sociis natoque penatibus et magnis dis parturient montes, nascetur ridiculus mus.</p>
  <div class="abs tabs"><span class="on">All</span><span>Work</span><span>Work List</span><span>Work</span></div>
  <div class="abs grid">
    <div class="g1" role="img" aria-label="Bird flying against a golden sunset sky"></div>
    <div class="g2" role="img" aria-label="Frosted tree in a snowy landscape"></div>
    <div class="g3"><div class="ov"><div class="eye"></div><b>Labore et dolore magnam</b><span>Webcraft</span></div></div>
    <div class="g4" role="img" aria-label="Hands holding a camera among bokeh lights"></div>
    <div class="g5" role="img" aria-label="Football player on a green field"></div>
    <div class="g6" role="img" aria-label="Stone gargoyles overlooking a city"></div>
    <div class="g7" role="img" aria-label="Seated figure in a conical hat"></div>
    <div class="g8" role="img" aria-label="White stork in flight on green"></div>
  </div>

  <h2 class="abs sec-title" style="top:925px">TESTIMONIALS</h2>
  <div class="abs quote" style="left:73px;top:970px">Lorem ipsum dolor sit amet, consectetuer adipiscing elit. Aenean commodo ligula eget dolor. Aenean massa. Cum sociis natoque penatibus et magnis dis parturient montes, nascetur ridiculus mus. Donec quam felis, ultricies nec, pellentesque eu, pretium quis, sem.</div>
  <div class="abs person" style="left:73px;top:1024px"><i></i>Name, Company</div>
  <div class="abs quote" style="left:262px;top:970px">Lorem ipsum dolor sit amet, consectetuer adipiscing elit. Aenean commodo ligula eget dolor. Aenean massa. Cum sociis natoque penatibus et magnis dis parturient montes, nascetur ridiculus mus. Donec quam felis, ultricies nec, pellentesque eu, pretium quis, sem.</div>
  <div class="abs person" style="left:262px;top:1024px"><i></i>NAME, Company</div>
  <div class="abs t-dots"><i class="on"></i><i></i><i></i><i></i></div>

  <footer class="abs footer">
    <div class="fcol" style="left:53px;width:85px">
      <h5 style="font-weight:700">Business Name</h5>
      <p>Far far away, behind the word mountains, far from the countries Vokalia and Consonantia, there live the blind texts. Separated they live in Bookmarksgrove right at the coast of the Semantics, a large language ocean. A small river named Duden flows by their place and supplies it with the necessary regelialia.</p>
    </div>
    <div class="fcol" style="left:148px;width:86px">
      <h5>Contact</h5>
      <p style="margin-bottom:6px">Lorem ipsum dolor sit amet, consectetuer adipiscing elit. Aenean commodo ligula eget dolor.</p>
      <div class="contact-row"><svg width="5" height="6" viewBox="0 0 5 6"><path d="M2.5 6L.5 3a2 2 0 1 1 4 0z" fill="#4aa3df"/></svg>Riffa, Bahrain</div>
      <div class="contact-row"><svg width="5" height="4" viewBox="0 0 5 4"><rect width="5" height="4" fill="#4aa3df"/><path d="M0 0l2.5 2L5 0" stroke="#2b3a44" stroke-width=".5" fill="none"/></svg>hello@brightmoorcare.bh</div>
      <div class="contact-row"><svg width="5" height="5" viewBox="0 0 5 5"><path d="M1 0l1 1.3-.6.8a3 3 0 0 0 1.5 1.5l.8-.6L5 4l-.8 1C2 5 0 3 0 .8z" fill="#4aa3df"/></svg>+973 1700 4821</div>
    </div>
    <div class="fcol" style="left:242px;width:92px">
      <h5>Latest Tweets</h5>
      <div class="tweet"><i></i><p>Curabitur felis nibh, lacinia non rhoncus vel, lobortis et lorem. Class aptent taciti sociosqu ad litora torquent per conubia nostra, per inceptos himenae.<br><em>5 Hours Ago</em></p></div>
      <div class="tweet"><i></i><p>Curabitur felis nibh, lacinia non rhoncus vel, lobortis et lorem. Class aptent taciti sociosqu ad litora torquent per<br><em>6 Hours Ago</em></p></div>
    </div>
    <div class="fcol" style="left:341px;width:90px">
      <h5>News Letter</h5>
      <p>Type your email address below and recive our daily news letter for free</p>
      <div class="news"><span>Email Address</span><b>Submit</b></div>
    </div>
  </footer>
  <div class="abs bottom"><p>All rights reserved.</p><div class="social"><i></i><i></i><i></i></div></div>

</div>
</body>
</html>
```